electrical contractor business card for professional modern company

I need a business card design for an electrical contractors business. I do all kinds of electricical work from new homes, air conditioning, data and communications. I have a logo design i want on it and have a good idea in my head of what i want it to look like. I like simple yet bold and professional looking. All black background is a must

Target Market(s)

Anyone needing electrical work done

Industry/Entity Type

Electrical

Contact Information for Business Card

company name- KPR Electrical and Data
person name-brian holloway
phone number- 0491 358 207
website-kprelec.com.au

Font styles to use
Sans Serif

Requirements
Must have
• email
• website
• logo
• name
• phone number
• list of work i do:
• -electrical
• -air-conditioning
• -data/communications
• -cctv/security
• -domestic/commercial/industrial
• -24hr emergency breakdown repair
Nice to have
• i would like the logo on the front side in the centre taking up most of the card with black background.
• on the rear i want the list of work i do with company info i.e. email, website, my name, phone number. rear of card also black background with orange writing to match the orange in the logo

```html
<!DOCTYPE html>
<html lang="en">
<head>
<meta charset="utf-8">
<title>KPR Electrical and Data – Business Card</title>
<link rel="stylesheet" href="https://fonts.googleapis.com/css2?family=Exo+2:wght@400;500;600&display=swap">
<style>
  :root {
    --backdrop: #3b342e;
    --card-black: #070707;
    --orange: #f0892a;
    --orange-soft: #e9a04a;
    --gold: #f3c53a;
    --grey: #8a8a8a;
  }
  * { box-sizing: border-box; margin: 0; padding: 0; }
  html, body {
    width: 1200px;
    height: 900px;
    overflow: hidden;
  }
  body {
    background: var(--backdrop);
    font-family: "Exo 2", sans-serif;
    position: relative;
  }
  .card {
    position: absolute;
    top: 285px;
    width: 540px;
    height: 330px;
    background: var(--card-black);
    border-radius: 4px;
    overflow: hidden;
    box-shadow: 0 18px 40px rgba(0,0,0,.45);
  }
  .card--info { left: 40px; }
  .card--brand { left: 620px; }

  /* Info side */
  .info-arcs {
    position: absolute;
    left: 0; top: 0;
    width: 540px; height: 330px;
  }
  .contact {
    position: absolute;
    right: 30px;
    top: 28px;
    text-align: right;
  }
  .contact__name {
    color: var(--gold);
    font-size: 30px;
    font-weight: 500;
    letter-spacing: .5px;
    line-height: 1.1;
  }
  .contact__line {
    color: var(--orange);
    font-size: 16px;
    line-height: 1.5;
    display: flex;
    justify-content: flex-end;
    align-items: center;
    gap: 8px;
  }
  .contact__icon {
    width: 13px; height: 13px;
    border-radius: 3px;
    background: var(--orange);
    display: inline-block;
  }
  .info-brand {
    position: absolute;
    right: 30px;
    top: 150px;
    display: flex;
    align-items: center;
    gap: 8px;
    color: var(--orange);
    font-size: 15px;
    font-weight: 600;
    letter-spacing: 1px;
    text-transform: uppercase;
  }
  .brand-dot {
    width: 12px; height: 12px;
    border-radius: 50%;
    background: var(--orange);
  }
  .services {
    position: absolute;
    left: 205px;
    bottom: 22px;
    list-style: none;
  }
  .services__item {
    color: var(--orange-soft);
    font-size: 16px;
    line-height: 1.45;
    display: flex;
    align-items: center;
    gap: 9px;
  }
  .services__item::before {
    content: "";
    width: 9px; height: 9px;
    border: 1.5px solid var(--orange-soft);
    border-radius: 50%;
  }

  /* Brand side */
  .brand-rule {
    position: absolute;
    left: 28px;
    right: 28px;
    height: 2px;
    background: var(--orange);
  }
  .brand-rule--top { top: 26px; }
  .brand-rule--bottom { bottom: 26px; }
  .brand-rule::before, .brand-rule::after {
    content: "";
    position: absolute;
    top: -2px;
    width: 6px; height: 6px;
    background: var(--orange);
  }
  .brand-rule::before { left: -3px; }
  .brand-rule::after { right: -3px; }
  .brand-mark {
    position: absolute;
    inset: 0;
    display: flex;
    align-items: center;
    justify-content: center;
    gap: 14px;
    color: var(--orange);
    font-size: 30px;
    font-weight: 600;
    letter-spacing: 1.5px;
    text-transform: uppercase;
  }
  .brand-mark .brand-dot { width: 22px; height: 22px; }
</style>
</head>
<body>
  <section class="card card--info" aria-label="Business card, contact side">
    <svg class="info-arcs" viewBox="0 0 540 330" aria-hidden="true">
      <circle cx="-10" cy="215" r="150" fill="none" stroke="var(--orange)" stroke-width="34"/>
      <circle cx="-10" cy="215" r="95" fill="none" stroke="var(--orange)" stroke-width="24"/>
    </svg>

    <div class="contact">
      <p class="contact__name">brian holloway</p>
      <p class="contact__line">0491 358 207 <span class="contact__icon"></span></p>
      <p class="contact__line">www.kprelec.com.au <span class="contact__icon"></span></p>
    </div>

    <div class="info-brand"><span class="brand-dot"></span>KPR Electrical and Data</div>

    <ul class="services">
      <li class="services__item">Electrical</li>
      <li class="services__item">Air-conditioning</li>
      <li class="services__item">Data/communications</li>
      <li class="services__item">Cctv/security</li>
      <li class="services__item">Domestic/commercial/industrial</li>
      <li class="services__item">24hr emergency breakdown repair</li>
    </ul>
  </section>

  <section class="card card--brand" aria-label="Business card, brand side">
    <div class="brand-rule brand-rule--top"></div>
    <div class="brand-mark"><span class="brand-dot"></span>KPR Electrical and Data</div>
    <div class="brand-rule brand-rule--bottom"></div>
  </section>
</body>
</html>
```